New Branding Business Card Design

Redesign business card according to new branding update.

** The design received so far are single color + BLACK.
I'd encourage designer to use different tones of blue / purple as described in the Designer Brief color palette

Target Market(s)

International

Industry/Entity Type

Medical Equipment

Contact Information for Business Card

Logo on one side (Designer can decide if they want to move certain info from the other side to save space)

Main body info (company name, individual name in both English and Chinese, contact info etc) on the other
Prefer a 'cleaner' layout - vs 'all over the place'
Prefer flush left alignment

Font styles to use
Sans Serif

Requirements
Must have
• Key info
• (Company name (English)): VORAK (HK) Limited
• (Name (English)): Martin L. Osei
• (Credential): FCPA, FHKSI
• (Title): Founder, Managing Director & CEO
• For the following info, designers decide whether to use colon or no colon, stroke separator, or use icon gfx for T (for telephone fixed line, M for mobile etc.)
• T: +852 2741 VORAK / +852 2741 5317
• M: +852 9473 6215 / + 86 139 4527 3916
• E: martin.l.osei@vorak-example.hk
Nice to have
• Depending on the space and spacing available designers can add or use fuller title and other info
• Title: Chairman of the Executive Committee, Founder, Managing Director & CEO
• (Name (Chinese)): 梁文浩
Should not have
• One of our business entities a long company name that cannot be broken into 2 lines
• makes vertical implementation almost impossible

```html
<!DOCTYPE html>
<html lang="en">
<head>
<meta charset="utf-8">
<title>VORAK Business Card</title>
<link rel="stylesheet" href="https://fonts.googleapis.com/css2?family=Lato:wght@400;700;900&display=swap">
<style>
  :root {
    --purple: #5b2d82;
    --charcoal: #2e2d30;
    --white: #ffffff;
    --ink: #2b2b2b;
    --backdrop: #e6e5e8;
  }
  * { margin: 0; padding: 0; box-sizing: border-box; }
  html, body {
    width: 1200px; height: 900px; overflow: hidden;
    background: var(--backdrop);
    font-family: "Lato", sans-serif;
  }
  .stage {
    position: relative; width: 1200px; height: 900px;
  }
  .card {
    position: absolute; left: 280px; width: 640px; height: 370px;
    border-radius: 30px; overflow: hidden;
    box-shadow: 0 10px 28px rgba(0,0,0,0.18);
  }
  .card--front { top: 45px; background: var(--purple); display: flex; align-items: center; justify-content: center; }
  .card--back { top: 470px; background: var(--white); }

  .brand-mark {
    color: var(--white); font-weight: 900; font-size: 84px; letter-spacing: 6px;
  }
  .swoosh { position: absolute; inset: 0; width: 100%; height: 100%; }

  .details { position: absolute; left: 44px; top: 38px; }
  .brand-small {
    color: var(--purple); font-weight: 900; font-size: 26px; letter-spacing: 2px;
  }
  .person-name {
    margin-top: 26px; color: var(--purple); font-weight: 900; font-size: 38px; line-height: 1;
  }
  .credential { margin-top: 8px; font-size: 13px; color: var(--ink); }
  .job-title { margin-top: 2px; font-size: 16px; color: var(--purple); }

  .contacts { margin-top: 20px; display: grid; grid-template-columns: 26px auto; row-gap: 12px; column-gap: 14px; align-items: center; }
  .contact-icon { width: 20px; height: 20px; }
  .contact-lines { font-size: 14px; line-height: 1.3; color: var(--purple); }
</style>
</head>
<body>
<div class="stage">
  <section class="card card--front">
    <span class="brand-mark">VORAK</span>
  </section>

  <section class="card card--back">
    <svg class="swoosh" viewBox="0 0 640 370" aria-hidden="true">
      <path d="M330 0 Q580 70 596 370 L640 370 L640 0 Z" fill="var(--charcoal)"/>
      <path d="M366 0 Q600 60 640 322 L640 0 Z" fill="var(--purple)" stroke="var(--white)" stroke-width="4"/>
    </svg>

    <div class="details">
      <div class="brand-small">VORAK</div>
      <h1 class="person-name">Martin L. Osei</h1>
      <p class="credential">FCPA, FHKSI</p>
      <p class="job-title">Founder, Managing Director &amp; CEO</p>

      <div class="contacts">
        <svg class="contact-icon" viewBox="0 0 20 20" aria-label="Telephone">
          <path d="M2 6 Q10 1 18 6 L16 8 L13 7 L13 5 Q10 4 7 5 L7 7 L4 8 Z" fill="var(--ink)"/>
          <rect x="4" y="9" width="12" height="8" rx="1.5" fill="var(--ink)"/>
          <circle cx="10" cy="13" r="2.2" fill="var(--white)"/>
        </svg>
        <div class="contact-lines">+852 2741 VORAK<br>+852 2741 5317</div>

        <svg class="contact-icon" viewBox="0 0 20 20" aria-label="Mobile">
          <rect x="5" y="1.5" width="10" height="17" rx="2" fill="none" stroke="var(--ink)" stroke-width="1.6"/>
          <circle cx="10" cy="15.5" r="1" fill="var(--ink)"/>
        </svg>
        <div class="contact-lines">+852 9473 6215<br>+ 86 139 4527 3916</div>

        <svg class="contact-icon" viewBox="0 0 20 20" aria-label="Email">
          <rect x="2" y="4.5" width="16" height="11" fill="var(--ink)"/>
          <path d="M2 4.5 L10 11 L18 4.5" fill="none" stroke="var(--white)" stroke-width="1.2"/>
        </svg>
        <div class="contact-lines">martin.l.osei@vorak-example.hk</div>
      </div>
    </div>
  </section>
</div>
</body>
</html>
```